Hair Care; Beauty Store

We need an E Commerce website with shopping cart functionality. An update of our other website www.velmarshopwares.com. A website we like the look, feel and functionality is: www.quorvashelf.com
The key functionality needed is:
• Shopping cart with Secure payment plugin:
1. Zentrix
• Blog with images and video postings
• Rotating Banner on homepage like www.quorvashelf.com
• Brindlow, Scovamel, Lumoraxe, driftcast updates (To and from option)
• Newsletter sign up (VIP Club)
• CRM – 8 step follow through (Ability to add this plug-in later)
• Discount codes
• Landing Page popup on first visit to sign up for VIP Club
• Newsletter
1. Create newsletter on website
2. Newsletter sent to subscribers
3. Opt out functionality
• Cpanel
• WYSIWYG editing
• WooCommerce or Virtue Mart cart
• Mobile compatible – Kelphone, Oslab and Mobile phones
• SEO
• Google Analytics
• Advertising windows. (time measured campaigns, Rotating)
• Search
• Required pages
1. Contact Us
2. Ordering Information
3. Return Policy
4. Guarantee
5. Testimonials – (With image)
-Reviews (Verified) – with product links like www.quorvashelf.com
6. Our Products
- Hair Care
- Beauty
- Mind and Soul

Target Market(s)

Shoppers

Industry/Entity Type

Hair And Beauty

Number of Pages Required

5+ page

Font styles to use
Sans Serif

Colors
9ccb3b
fbed22
0493ce
0555a3
e34197
a54499
6b449b
f37122

Requirements
Must have
• Shopping Cart
• Newsletter
• Advertising Banner
• Landing page pop up/Newsletter sign up
• Zentrix payment
• Search
• Blog
• WYSIWYG Cpanel
Nice to have
• CRM add on

```html
<!DOCTYPE html>
<html lang="en">
<head>
<meta charset="utf-8">
<title>Velmar Beauty – Hair Care &amp; Beauty Store</title>
<link rel="stylesheet" href="https://fonts.googleapis.com/css2?family=Montserrat:wght@400;600;700&family=Open+Sans:wght@400;600;700&display=swap">
<style>
:root{
  --pink:#e34197;
  --green:#9ccb3b;
  --brand:#1f5a3a;
  --ink:#1b1b1b;
  --text:#555;
  --muted:#999;
  --line:#e3e3e3;
  --topbar:#f1f1f1;
  --dark:#1d1d1d;
  --dark-2:#262626;
  --white:#fff;
}
*{box-sizing:border-box;margin:0;padding:0}
html,body{width:1200px;height:4255px;overflow:hidden}
body{font-family:"Open Sans",Arial,sans-serif;color:var(--text);background:var(--white);position:relative}
h1,h2,h3,h4,.heading{font-family:"Montserrat",Arial,sans-serif;color:var(--ink)}
a{color:inherit;text-decoration:none}
ul{list-style:none}
.abs{position:absolute}
.btn{display:inline-block;background:var(--pink);color:var(--white);font:700 13px "Montserrat",sans-serif;letter-spacing:.5px;text-transform:uppercase;padding:11px 24px}

/* top bar */
.topbar{position:absolute;left:0;top:0;width:1200px;height:31px;background:var(--topbar);font-size:11px;color:#777}
.topbar .links{position:absolute;left:100px;top:9px;display:flex;gap:40px}
.topbar .search{position:absolute;left:800px;top:6px;width:130px;height:19px;border-bottom:1px solid #ccc;font-size:11px;color:#888;padding-top:2px}
.topbar .search svg{position:absolute;right:0;top:3px}
.topbar .cart{position:absolute;left:965px;top:8px;display:flex;gap:8px;align-items:center}

/* header */
.header{position:absolute;left:0;top:31px;width:1200px;height:100px;background:var(--white)}
.logo{position:absolute;left:100px;top:22px;display:flex;align-items:center;gap:12px;font:700 28px/1 "Montserrat",sans-serif;color:var(--brand);letter-spacing:1px}
.logo .mark{width:22px;height:22px;border-radius:50%;background:var(--brand)}
.nav{position:absolute;left:585px;top:43px;display:flex;gap:0;font:600 12px "Montserrat",sans-serif;color:var(--ink)}
.nav li{position:absolute;white-space:nowrap}

/* hero */
.hero{position:absolute;left:0;top:131px;width:1200px;height:561px;background:radial-gradient(ellipse at 65% 40%,#6a5246 0%,#3b2e29 35%,#1e1a19 75%)}
.hero .copy{position:absolute;left:102px;top:318px;color:var(--white)}
.hero .copy .l1{font:700 38px "Montserrat",sans-serif;letter-spacing:1px}
.hero .copy .l2{font:400 34px "Montserrat",sans-serif;color:#ddd;margin-top:8px;letter-spacing:1px}
.hero .copy .l3{font:400 48px "Montserrat",sans-serif;letter-spacing:2px;margin-top:4px}
.hero .arrow{position:absolute;top:262px;width:40px;height:40px;border-radius:50%;border:1px solid rgba(255,255,255,.35)}

/* welcome */
.welcome{position:absolute;left:0;top:692px;width:1200px;height:420px;text-align:center}
.welcome h2{position:absolute;left:0;width:1200px;top:86px;font-size:37px;line-height:48px;font-weight:700}
.welcome .rule{position:absolute;left:585px;top:196px;width:30px;height:3px;background:var(--brand)}
.welcome p{position:absolute;left:200px;width:800px;top:222px;font-size:13px;line-height:22px;color:#888}
.welcome .btn{position:absolute;left:508px;top:293px;width:184px;text-align:center}

/* feature panels */
.features{position:absolute;left:0;top:1112px;width:1200px;height:494px;display:flex}
.feature{position:relative;width:400px;height:494px}
.feature .title{position:absolute;left:40px;top:334px;color:var(--white);font:700 21px/32px "Montserrat",sans-serif}
.feature .btn{position:absolute;left:40px;top:414px;padding:10px 18px;font-size:12px}

/* products */
.products{position:absolute;left:0;top:1606px;width:1200px;height:720px}
.section-title{position:absolute;left:0;width:1200px;text-align:center;font:700 37px "Montserrat",sans-serif;color:var(--ink)}
.tabs{position:absolute;left:0;width:1200px;top:176px;display:flex;justify-content:center;gap:86px;font:700 13px "Montserrat",sans-serif;color:var(--ink)}
.tabs .active{color:var(--green)}
.slider-arrow{position:absolute;top:380px;width:56px;height:56px;border:2px solid #333;background:var(--white);display:flex;align-items:center;justify-content:center}
.product{position:absolute;top:250px;width:220px;text-align:center}
.product .shot{height:240px;position:relative}
.product .shot .btn{position:absolute;left:50%;top:96px;transform:translateX(-50%);padding:9px 18px;font-size:12px}
.product .name{margin-top:40px;font:700 13px/20px "Montserrat",sans-serif;color:var(--ink)}
.product .price{margin-top:16px;font:700 15px "Montserrat",sans-serif;color:var(--ink);display:flex;justify-content:center;gap:30px}
.product .price s{color:#999;font-weight:400}

/* testimonial */
.testimonial{position:absolute;left:0;top:2326px;width:1200px;height:531px;background:#262626}
.testimonial .photo{position:absolute;left:560px;top:0;width:640px;height:531px;background:radial-gradient(ellipse at 45% 45%,#8a5a34 0%,#5a3a22 30%,#262626 70%)}
.testimonial h2{position:absolute;left:108px;top:90px;color:var(--white);font:700 56px/62px "Montserrat",sans-serif}
.testimonial h2 span{display:block;font-size:42px;line-height:54px}
.testimonial .quote{position:absolute;left:120px;top:250px;width:400px;font:italic 13px/24px "Open Sans",sans-serif;color:#9a9a9a}
.testimonial .qmark{position:absolute;font:700 40px "Montserrat",sans-serif;color:#555}
.testimonial .author{position:absolute;left:108px;top:380px;display:flex;align-items:center;gap:18px}
.testimonial .avatar{width:72px;height:72px;border-radius:50%;background:linear-gradient(135deg,#c98a63,#6d3e2a);border:3px solid #3a3a3a}
.testimonial .author b{display:block;color:var(--white);font:700 12px "Montserrat",sans-serif}
.testimonial .author small{color:#888;font-size:11px}
.testimonial .dots{position:absolute;left:500px;top:410px;display:flex;gap:6px}
.testimonial .dots i{width:7px;height:7px;border-radius:50%;background:#666}

/* blog */
.blog{position:absolute;left:0;top:2857px;width:1200px;height:979px}
.blog .sub{position:absolute;left:0;width:1200px;top:133px;text-align:center;font-size:12px;color:#888}
.post{position:absolute;top:193px;width:323px}
.post .img{height:235px}
.post h4{margin-top:30px;font:700 13px "Montserrat",sans-serif}
.post .date{margin-top:10px;font-size:11px;color:#999;display:flex;gap:8px;align-items:center}
.post p{margin-top:10px;font-size:12px;line-height:21px;color:#999}
.feed-head{position:absolute;left:100px;top:625px;right:97px;height:40px}
.feed-head h4{position:absolute;left:0;top:12px;font:700 14px "Montserrat",sans-serif}
.feed-head h4 small{font:400 11px "Open Sans",sans-serif;color:#999;margin-left:10px}
.feed-head .connect{position:absolute;right:0;top:0;background:#d22;color:var(--white);font:600 13px "Open Sans",sans-serif;padding:10px 16px;display:flex;gap:10px;align-items:center}
.feed-head .connect i{width:16px;height:16px;border-radius:50%;background:var(--white)}
.feed{position:absolute;left:100px;top:675px;width:1003px;display:grid;grid-template-columns:repeat(9,1fr);gap:12px 8px}
.feed div{height:119px}

/* footer */
.footer{position:absolute;left:0;top:3836px;width:1200px;height:419px;background:var(--dark);color:#9a9a9a;font-size:12px}
.footer h4{color:var(--white);font:700 14px "Montserrat",sans-serif;margin-bottom:28px}
.fcol{position:absolute;top:75px}
.fcol li{margin-bottom:13px}
.fcol .email{width:272px;height:36px;border:1px solid #444;margin-top:20px;padding:10px 12px;font-size:11px;color:#888}
.fcol .btn{margin-top:24px;padding:10px 22px;font-size:11px}
.contact li{display:flex;gap:12px;align-items:flex-start;line-height:19px}
.footer .bottom{position:absolute;left:100px;right:100px;top:340px;border-top:1px solid #333;padding-top:26px;font-size:11px;display:flex;justify-content:space-between}
.footer .bottom b{color:var(--white);font-weight:600}
.footer .bottom ul{display:flex;gap:70px}
</style>
</head>
<body>

<div class="topbar">
  <ul class="links"><li>My Account</li><li>Compare</li><li>Wishlist</li><li>Delivery</li><li>Help</li></ul>
  <div class="search">Search by Keyword
    <svg width="12" height="12" viewBox="0 0 12 12"><circle cx="5" cy="5" r="4" fill="none" stroke="#888" stroke-width="1.5"/><line x1="8" y1="8" x2="11" y2="11" stroke="#888" stroke-width="1.5"/></svg>
  </div>
  <div class="cart">
    <svg width="16" height="13" viewBox="0 0 16 13"><path d="M1 1h3l2 8h8l2-6H5" fill="none" stroke="#f0a020" stroke-width="1.6"/><circle cx="7" cy="11.5" r="1.3" fill="#f0a020"/><circle cx="13" cy="11.5" r="1.3" fill="#f0a020"/></svg>
    Your cart is : 0 items
  </div>
</div>

<header class="header">
  <a class="logo" href="#"><span class="mark"></span>VELMAR BEAUTY</a>
  <ul class="nav">
    <li style="left:0">HOME</li>
    <li style="left:120px">ABOUT US</li>
    <li style="left:234px">SHOP</li>
    <li style="left:336px">BLOG</li>
    <li style="left:440px">CONTACT US</li>
  </ul>
</header>

<section class="hero" role="img" aria-label="Banner photograph of a woman with long, dark, voluminous wavy hair">
  <span class="arrow" style="left:40px"></span>
  <span class="arrow" style="left:1120px"></span>
  <div class="copy">
    <div class="l1">VELMAR BEAUTY</div>
    <div class="l2">BEAUTIFUL AND HEALTHY HAIR</div>
    <div class="l3">STARTS HERE</div>
  </div>
</section>

<section class="welcome">
  <h2>WELCOME TO<br>VELMAR BEAUTY</h2>
  <span class="rule"></span>
  <p>Velmar Beauty, Inc offers products made with botanical ingredients and all our formulas offer the best of both science and nature, and manufactures it unique.</p>
  <a class="btn" href="#">View all category</a>
</section>

<section class="features">
  <div class="feature" role="img" aria-label="Photo of a woman with golden curly hair" style="background:linear-gradient(160deg,#8a6a4e,#4a3528 60%,#2a201a)">
    <div class="title">WE HAVE A PASSION FOR<br>YOUR HAIR CARE</div>
    <a class="btn" href="#">View all category</a>
  </div>
  <div class="feature" role="img" aria-label="Photo of a man with a styled undercut haircut" style="background:linear-gradient(160deg,#3d4650,#1f2529 60%,#131618)">
    <div class="title" style="top:350px">100 PREMIUM QUALITY</div>
    <a class="btn" href="#">View all category</a>
  </div>
  <div class="feature" role="img" aria-label="Black and white photo of a woman with short platinum curls" style="background:linear-gradient(160deg,#7a7a7a,#3a3a3a 60%,#1a1a1a)">
    <div class="title">WE PLEDGE TO CARE FOR<br>YOUR HAIR!</div>
    <a class="btn" href="#">View all category</a>
  </div>
</section>

<section class="products">
  <h2 class="section-title" style="top:92px">POPULAR PRODUCTS</h2>
  <ul class="tabs"><li class="active">FEATURED PRODUCTS</li><li>SPECIAL PRODUCTS</li><li>OFFER PRODUCTS</li></ul>

  <div class="slider-arrow" style="left:51px"><svg width="22" height="12" viewBox="0 0 22 12"><path d="M21 6H2M7 1L2 6l5 5" fill="none" stroke="#222" stroke-width="2"/></svg></div>
  <div class="slider-arrow" style="left:1091px"><svg width="22" height="12" viewBox="0 0 22 12"><path d="M1 6h19M15 1l5 5-5 5" fill="none" stroke="#222" stroke-width="2"/></svg></div>

  <div class="product" style="left:140px">
    <div class="shot" role="img" aria-label="Brow primer tube with white and pink box" style="background:linear-gradient(90deg,#fff 20%,#eee 40%,#f6d7e7 55%,#fff 75%)"><a class="btn" href="#">Buy now</a></div>
    <div class="name">CLEARLINE BROWS<br>Botanical Primer Chocolate<br>Tint 0.7 Oz</div>
    <div class="price"><s>$34.50</s><span>$28.50</span></div>
  </div>
  <div class="product" style="left:380px">
    <div class="shot" role="img" aria-label="Round jar of green-lidded hair treatment" style="background:radial-gradient(ellipse at 50% 55%,#cfe2b0 0%,#eef4e3 40%,#fff 65%)"></div>
    <div class="name">CLEARLINE BROWS<br>Botanical Primer Chocolate<br>Tint 0.7 Oz</div>
    <div class="price"><s>$34.50</s><span>$28.50</span></div>
  </div>
  <div class="product" style="left:620px">
    <div class="shot" role="img" aria-label="Gold-lidded brow pomade jar with brush" style="background:radial-gradient(ellipse at 50% 55%,#d9b65a 0%,#f3e6c2 40%,#fff 65%)"></div>
    <div class="name">CLEARLINE BROWS<br>Botanical Primer Chocolate<br>Tint 0.7 Oz</div>
    <div class="price"><s>$34.50</s><span>$28.50</span></div>
  </div>
  <div class="product" style="left:860px">
    <div class="shot" role="img" aria-label="Green bottle of shampoo with pink label" style="background:radial-gradient(ellipse at 50% 55%,#3c7a3e 0%,#b9d6b0 35%,#fff 62%)"></div>
    <div class="name">CLEARLINE BROWS<br>Botanical Primer Chocolate<br>Tint 0.7 Oz</div>
    <div class="price"><s>$34.50</s><span>$28.50</span></div>
  </div>
</section>

<section class="testimonial">
  <div class="photo" role="img" aria-label="Photo of a woman with voluminous copper curly hair"></div>
  <h2>WHAT<span>OUR CLIENT'S SAY</span></h2>
  <span class="qmark" style="left:96px;top:230px">“</span>
  <p class="quote">Being a natural blonde, my scalp is extremely sensitive. I often purchase shampoo only to find out I can not use them. As soon as I opened the top of this shampoo, the scent was so refreshing, I had no...</p>
  <span class="qmark" style="left:518px;top:320px">”</span>
  <div class="author">
    <div class="avatar" role="img" aria-label="Client portrait"></div>
    <div><b>NESSA PALORIN</b><small>Happy Client</small></div>
  </div>
  <div class="dots"><i></i><i></i></div>
</section>

<section class="blog">
  <h2 class="section-title" style="top:62px">NEWS &amp; BLOG</h2>
  <p class="sub">Lorem ipsum is simply dummy text of the printing and typesetting industry.</p>

  <article class="post" style="left:100px">
    <div class="img" role="img" aria-label="Photo of a man checking his hairline" style="background:linear-gradient(135deg,#e9e3dc,#b48c6e 60%,#7a5a44)"></div>
    <h4>ANTI-HAIR LOSS ROUTINE</h4>
    <div class="date"><svg width="11" height="11" viewBox="0 0 11 11"><rect x=".5" y="1.5" width="10" height="9" fill="none" stroke="#aaa"/><line x1=".5" y1="4" x2="10.5" y2="4" stroke="#aaa"/></svg>March 10, 2016</div>
    <p>Every day we are seeing lots of commercials promising great hair just if you'll favor this or that brand.</p>
  </article>
  <article class="post" style="left:440px">
    <div class="img" role="img" aria-label="Photo of two women with big curly hair" style="background:linear-gradient(135deg,#2a2220,#6b4a36 50%,#a07a5c)"></div>
    <h4>ANTI-HAIR LOSS ROUTINE</h4>
    <div class="date"><svg width="11" height="11" viewBox="0 0 11 11"><rect x=".5" y="1.5" width="10" height="9" fill="none" stroke="#aaa"/><line x1=".5" y1="4" x2="10.5" y2="4" stroke="#aaa"/></svg>March 10, 2016</div>
    <p>Every day we are seeing lots of commercials promising great hair just if you'll favor this or that brand.</p>
  </article>
  <article class="post" style="left:780px">
    <div class="img" role="img" aria-label="Photo of a woman on a beach at dusk" style="background:linear-gradient(180deg,#cfc4b4,#a89680 55%,#6d5e4e)"></div>
    <h4>ANTI-HAIR LOSS ROUTINE</h4>
    <div class="date"><svg width="11" height="11" viewBox="0 0 11 11"><rect x=".5" y="1.5" width="10" height="9" fill="none" stroke="#aaa"/><line x1=".5" y1="4" x2="10.5" y2="4" stroke="#aaa"/></svg>March 10, 2016</div>
    <p>Every day we are seeing lots of commercials promising great hair just if you'll favor this or that brand.</p>
  </article>

  <div class="feed-head">
    <h4>SCOVAMEL FEED<small>2,026 People members</small></h4>
    <a class="connect" href="#"><i></i>Connect with Scovamel</a>
  </div>
  <div class="feed" role="img" aria-label="Grid of hairstyle photos from the social feed">
    <div style="background:linear-gradient(135deg,#3a2a22,#7a5a44)"></div>
    <div style="background:linear-gradient(135deg,#c9b9a8,#6e5646)"></div>
    <div style="background:linear-gradient(135deg,#5a3a2a,#b08060)"></div>
    <div style="background:linear-gradient(135deg,#2a2a2a,#6a6a6a)"></div>
    <div style="background:linear-gradient(135deg,#ddd,#a0a0a0)"></div>
    <div style="background:linear-gradient(135deg,#7a6a5a,#3a302a)"></div>
    <div style="background:linear-gradient(135deg,#e8d8c8,#9a7a5a)"></div>
    <div style="background:linear-gradient(135deg,#c05a3a,#4a2a1a)"></div>
    <div style="background:linear-gradient(135deg,#2a2220,#8a6a50)"></div>
    <div style="background:linear-gradient(135deg,#5a4a3a,#1a1410)"></div>
    <div style="background:linear-gradient(135deg,#a07a5a,#4a3020)"></div>
    <div style="background:linear-gradient(135deg,#c8c0b8,#6a6056)"></div>
    <div style="background:linear-gradient(135deg,#3a3030,#8a7060)"></div>
    <div style="background:linear-gradient(135deg,#b09070,#5a4030)"></div>
    <div style="background:linear-gradient(135deg,#e0d0c0,#7a6050)"></div>
    <div style="background:linear-gradient(135deg,#6a5040,#2a1e18)"></div>
    <div style="background:linear-gradient(135deg,#9a6a4a,#3a2418)"></div>
    <div style="background:linear-gradient(135deg,#4a4a4a,#1a1a1a)"></div>
  </div>
</section>

<footer class="footer">
  <div class="fcol" style="left:108px">
    <h4>GET 15% DISCOUNT COUPON</h4>
    <p style="width:280px;line-height:19px">Sign up for our newsletter and get the latest news and a 15% off coupon</p>
    <div class="email">Enter your email id</div>
    <a class="btn" href="#">Subscribe</a>
  </div>
  <div class="fcol contact" style="left:474px">
    <h4>CONTACT INFO</h4>
    <ul>
      <li style="width:220px">2280 Ferrow Lane, Suite 210<br>Dalmont, CA 90412</li>
      <li><svg width="12" height="12" viewBox="0 0 12 12"><path d="M2 1h3l1 3-2 1a7 7 0 003 3l1-2 3 1v3c-6 1-10-3-9-9z" fill="#999"/></svg>800-555-0142</li>
      <li><svg width="12" height="10" viewBox="0 0 12 10"><rect x=".5" y=".5" width="11" height="9" fill="none" stroke="#999"/><path d="M.5 .5l5.5 5 5.5-5" fill="none" stroke="#999"/></svg>info@velmarshopwares.com</li>
    </ul>
    <a class="btn" href="#" style="margin-top:10px">Contact</a>
  </div>
  <div class="fcol" style="left:757px">
    <h4>INFORMATION</h4>
    <ul><li>About Us</li><li>Delivery Information</li><li>Privacy &amp; Policy</li><li>Terms &amp; Conditions</li><li>Manufactures</li></ul>
  </div>
  <div class="fcol" style="left:976px">
    <h4>MY ACCOUNT</h4>
    <ul><li>My Account</li><li>Wish List</li><li>Site Map</li><li>Custom Service</li><li>Custom Link</li></ul>
  </div>
  <div class="bottom">
    <span>Copyright © 2016, <b>Velmar beauty</b>. All Rights Reserved.</span>
    <ul><li>Search Terms</li><li>Contact Us</li><li>Orders and Returns</li><li>Advanced Search</li><li>Blog</li></ul>
  </div>
</footer>

</body>
</html>
```